wine label design

i'm a fine wine store based in new zealand which buys quality bulk wine and bottles it, passing on the significant savings onto the customer. i require a brand name and design which is cool/ sharp and contempory. the wines will be all still wines, there won't be any sparkling wines under this brand. i've used brand names like harbourlight wine company for previous designs/label but want something more edgier. we thought about a brand name 'sky above the vines' or 'harbourlight wine co' but couldn't get a design to match the title of brand, if you have any thoughts on this send thru your design. take into account color they have to be bold as i am printing these thru a digital printer. the label is a wrap around design, the dimensions are approximately 80 or 90 mm high and 210 mm wide. have a look at these links, i think they have some x-factor to them: http://www.marlowvale.example/store/product_images/p/855/velora__34476_zoom.jpg: OR

http://static3.cellarfinder.example/images/labels/35/24/ember-in-the-fog-shiraz-petite-sirah-south-australia-10203524.jpg: OR

http://www.bottlebarn.example/ui/productimages/25223/25223_w240.jpg: OR

http://www.vintrail.example/images/viewWinery.php?pic=238291

Take into account i have to be able put a wine desription on the back label, barcode and a few technical details required by law. on the front label all i require is space to put the grape variety, area and vintage. i need the grape type to really stand out.
Updates

Reason: hi, the designs coming thru look good, just need a little more changes, also please read thru the brief, there are a few things i have noted such as label size etc etc

Target Market(s)

am after a label the cool/edgy/contempoary that appeals to the educated well off customer that willing to give something new a go by the look of the label that is cool and edgy.

Industry/Entity Type

Boutique

Requirements
Must have
• bold bold bold, it must stand out on the shelf
Nice to have
• a title/brand name that links what i'm doing, from what i'm doing the name 'harbourlight wine co' is probably best suited.
Should not have
• basic boring artwork and small text, the bigger the text the better

```html
<!DOCTYPE html>
<html lang="en">
<head>
<meta charset="utf-8">
<title>Sky Above the Vines – Wine Label</title>
<link rel="stylesheet" href="https://fonts.googleapis.com/css2?family=Rubik+Dirt&family=Questrial&display=swap">
<style>
  :root {
    --lime: #cdd815;
    --ink: #141414;
    --backdrop: #efefef;
  }
  * { margin: 0; padding: 0; box-sizing: border-box; }
  html, body {
    width: 1200px;
    height: 640px;
    overflow: hidden;
    background: var(--backdrop);
  }
  .canvas {
    position: relative;
    width: 1200px;
    height: 640px;
    display: flex;
    align-items: center;
    justify-content: center;
  }
  .label {
    width: 590px;
    height: 630px;
    display: flex;
    flex-direction: column;
  }
  .label__brand {
    flex: 0 0 478px;
    background: var(--lime);
    display: flex;
    align-items: center;
    justify-content: center;
  }
  .brand-name {
    font-family: "Rubik Dirt", "Arial Black", sans-serif;
    font-weight: 400;
    font-size: 118px;
    line-height: 104px;
    color: var(--ink);
    text-align: center;
    text-transform: uppercase;
    letter-spacing: 1px;
    padding-top: 6px;
  }
  .brand-name span { display: block; }
  .label__details {
    flex: 1;
    background: var(--ink);
    color: var(--lime);
    font-family: "Questrial", "Century Gothic", sans-serif;
    text-align: center;
    display: flex;
    flex-direction: column;
    justify-content: center;
    gap: 6px;
  }
  .wine-style { font-size: 27px; }
  .vintage { font-size: 30px; }
  .volume { font-size: 20px; }
</style>
</head>
<body>
  <main class="canvas">
    <section class="label">
      <div class="label__brand">
        <h1 class="brand-name">
          <span>Sky</span>
          <span>Above</span>
          <span>The</span>
          <span>Vines</span>
        </h1>
      </div>
      <div class="label__details">
        <p class="wine-style">Regional Red Dry Wine</p>
        <p class="vintage">2009</p>
        <p class="volume">e750ml</p>
      </div>
    </section>
  </main>
</body>
</html>
```